update company powerpoint deck - inject more power/personality into the deck

We would like a designer to provide us with a powerpoint template based on our brand guidelines. Current brand guidelines, colours and existing deck provided.
Current deck lacks punch. We really like our black and white elements - but need options for graphs, tables and charts. We potentially need more supplementary colours to what is currently in our brand guidelines.

Target Market(s)

listed companies - B2B. We are a management consulting company.

Industry/Entity Type

Consulting

Font styles to use
Serif
Sans Serif

Requirements
Must have
• Slides that are common for consulting companies.
The ability to use the deck as a report - not just a presentation format

```html
<!DOCTYPE html>
<html lang="en">
<head>
<meta charset="utf-8">
<title>Noraline — Consulting Deck Template</title>
<link href="https://fonts.googleapis.com/css2?family=Roboto+Slab:wght@400;700&family=Roboto:wght@400;500;700&display=swap" rel="stylesheet">
<style>
:root{
  --page:#d4d8df;
  --slide:#f6f7fa;
  --ink:#22242b;
  --dark:#272930;
  --muted:#8b8f99;
  --soft:#e4e7ec;
  --line:#d3d6dc;
  --teal:#2ec4b6;
  --white:#ffffff;
  --photo-a:#b9bdc4;
  --photo-b:#3b3e46;
}
*{margin:0;padding:0;box-sizing:border-box}
html,body{width:1200px;height:2840px;overflow:hidden;background:var(--page);font-family:'Roboto',Arial,sans-serif;color:var(--ink)}
.canvas{position:relative;width:1200px;height:2840px;overflow:hidden}
.deck{position:absolute;left:57px;top:-236px;display:grid;grid-template-columns:514px 514px;column-gap:57px;row-gap:30px;grid-auto-rows:289px}
.slide{position:relative;background:var(--slide);overflow:hidden}
.slide>*{position:absolute}
.slide.is-dark{background:var(--dark)}
.brand{left:25px;top:16px;font:500 6.5px 'Roboto',sans-serif;letter-spacing:.4px;color:var(--ink)}
.brand.light{color:var(--white)}
.footer-url{right:52px;bottom:14px;font-size:6px;color:var(--muted)}
.page-no{right:25px;bottom:14px;font-size:6px;font-weight:700;color:var(--ink)}
.tag{background:var(--teal);color:var(--white);font:700 5.5px 'Roboto',sans-serif;letter-spacing:.6px;padding:2px 5px;text-transform:uppercase}
.title{font:700 22px/29px 'Roboto Slab',Georgia,serif;color:var(--ink)}
.title.light{color:var(--white)}
.title.center{text-align:center}
.copy{font-size:6.5px;line-height:10px;color:var(--muted)}
.copy.light{color:#a9adb6}
.label{font:700 7px 'Roboto',sans-serif;color:var(--ink)}
.label.light{color:var(--white)}
.photo{background:linear-gradient(150deg,var(--photo-a),var(--photo-b))}
.photo.dim{background:linear-gradient(160deg,#6c7079,#1f2127)}
.photo.pale{background:linear-gradient(180deg,#eceef1,#c7cad0)}
.panel-dark{background:var(--dark)}
.stat{font:700 20px 'Roboto Slab',Georgia,serif;color:var(--ink)}
.stat.light{color:var(--white)}
.menu{left:55px;top:100px;width:110px}
.menu-item{position:relative;height:22px;margin-bottom:2px;background:var(--soft);font:500 6.5px/22px 'Roboto',sans-serif;padding-left:8px;color:var(--ink)}
.menu-item::after{content:"›";position:absolute;right:7px;color:var(--muted)}
.menu-item.active{background:var(--dark);color:var(--white)}
.service-box{border:1.5px solid var(--ink);width:109px;height:96px;padding:10px}
.service-box svg{display:block;margin-bottom:14px}
.service-card{top:162px;width:128px;height:83px;background:var(--soft);text-align:center;padding-top:14px}
.service-card.active{background:var(--dark)}
.service-card .label{font-size:5.5px;margin-top:6px}
.service-card .copy{font-size:5px;line-height:7px;padding:2px 10px 0}
.btn{display:inline-block;margin-top:5px;background:var(--white);color:var(--ink);font:700 5px 'Roboto',sans-serif;padding:3px 6px}
.bar-track{height:3px;background:var(--line);width:170px}
.bar-fill{height:3px;background:var(--ink)}
.check-row{left:230px;width:230px;display:flex;gap:8px}
.check-box{width:9px;height:9px;border:1.3px solid var(--ink);flex:none;margin-top:1px}
.check-box.on{background:var(--ink)}
.rule{height:1px;background:var(--ink)}
</style>
</head>
<body>
<div class="canvas">
<main class="deck">

  <!-- row 0 -->
  <section class="slide">
    <p class="footer-url">www.noraline.co</p><p class="page-no">14</p>
  </section>
  <section class="slide">
    <div class="rule" style="left:258px;top:40px;width:256px"></div>
    <p class="footer-url">www.noraline.co</p><p class="page-no">15</p>
  </section>

  <!-- row 1 -->
  <section class="slide">
    <p class="brand">NORALINE</p>
    <p class="tag" style="left:53px;top:53px">Our Concepts</p>
    <h2 class="title" style="left:53px;top:66px;width:190px">A business that makes nothing…</h2>
    <div class="photo" style="left:258px;top:0;width:127px;height:147px" role="img" aria-label="Street view of an old building"></div>
    <div class="photo dim" style="left:385px;top:0;width:129px;height:147px" role="img" aria-label="Aircraft tail on an airfield"></div>
    <div class="photo" style="left:0;top:147px;width:258px;height:142px" role="img" aria-label="Glass office tower seen from below"></div>
    <svg style="left:272px;top:160px" width="16" height="16" viewBox="0 0 16 16" fill="none" stroke="#22242b" stroke-width="1.3"><circle cx="6.5" cy="6.5" r="4.5"/><path d="M10 10l4.5 4.5"/></svg>
    <p class="label" style="left:272px;top:188px">Market Research</p>
    <p class="copy" style="left:272px;top:200px;width:105px">Clear insight into every market we enter with you.</p>
    <div class="panel-dark" style="left:385px;top:147px;width:129px;height:142px"></div>
    <svg style="left:398px;top:160px" width="18" height="14" viewBox="0 0 18 14" fill="none" stroke="#fff" stroke-width="1.2"><path d="M5 12h9a3.5 3.5 0 0 0 0-7 5 5 0 0 0-9.5 1A3 3 0 0 0 5 12z"/></svg>
    <p class="label light" style="left:398px;top:188px">Cloud Base</p>
    <p class="copy light" style="left:398px;top:200px;width:105px">Shared data for teams working across every office.</p>
    <p class="footer-url" style="color:#c0c3ca">www.noraline.co</p><p class="page-no" style="color:#fff">16</p>
  </section>

  <section class="slide">
    <p class="brand">NORALINE</p>
    <div class="service-box" style="left:130px;top:49px">
      <svg width="16" height="14" viewBox="0 0 16 14" fill="none" stroke="#22242b" stroke-width="1.2"><path d="M1 1h14v9H6l-3 3v-3H1z"/></svg>
      <p class="label" style="font-size:6px">Support Center</p><p class="copy" style="font-size:5px;line-height:7px">Help that answers within a day.</p>
    </div>
    <div class="service-box" style="left:239px;top:49px">
      <svg width="16" height="14" viewBox="0 0 16 14" fill="none" stroke="#22242b" stroke-width="1.2"><rect x="2" y="1" width="12" height="9"/><path d="M0 13h16"/></svg>
      <p class="label" style="font-size:6px">Online Center</p><p class="copy" style="font-size:5px;line-height:7px">Workshops run fully online.</p>
    </div>
    <div class="service-box" style="left:348px;top:49px">
      <svg width="12" height="15" viewBox="0 0 12 15" fill="none" stroke="#22242b" stroke-width="1.2"><path d="M6 1a5 5 0 0 0-3 9v2h6v-2a5 5 0 0 0-3-9zM4 14h4"/></svg>
      <p class="label" style="font-size:6px">Creative Design</p><p class="copy" style="font-size:5px;line-height:7px">Ideas shaped into clear plans.</p>
    </div>
    <div class="service-box" style="left:239px;top:149px">
      <svg width="15" height="15" viewBox="0 0 15 15" fill="none" stroke="#22242b" stroke-width="1.2"><circle cx="6" cy="6" r="4.5"/><path d="M9.5 9.5L14 14"/></svg>
      <p class="label" style="font-size:6px">Market Research</p><p class="copy" style="font-size:5px;line-height:7px">Data that guides each decision.</p>
    </div>
    <div class="service-box" style="left:348px;top:149px">
      <svg width="16" height="14" viewBox="0 0 16 14" fill="none" stroke="#22242b" stroke-width="1.2"><path d="M1 2l4.5-1.5 5 2L15 1v11l-4.5 1.5-5-2L1 12z M5.5 .5v11 M10.5 2.5v11"/></svg>
      <p class="label" style="font-size:6px">Business Trip</p><p class="copy" style="font-size:5px;line-height:7px">On-site visits across regions.</p>
    </div>
    <p class="tag" style="left:53px;top:181px">Our Services</p>
    <h2 class="title" style="left:53px;top:194px;width:180px;font-size:19px;line-height:25px">Featured Service Center</h2>
    <p class="footer-url">www.noraline.co</p><p class="page-no">17</p>
  </section>

  <!-- row 2 -->
  <section class="slide">
    <div class="photo dim" style="left:0;top:0;width:514px;height:130px" role="img" aria-label="Sea horizon under a cloudy sky"></div>
    <p class="brand light">NORALINE</p>
    <p class="tag" style="left:53px;top:44px">Concept Analysis</p>
    <h2 class="title light" style="left:53px;top:56px;width:175px">Business special concepts</h2>
    <p class="stat" style="left:53px;top:150px">90.</p>
    <p class="stat" style="left:205px;top:150px">85.</p>
    <p class="stat" style="left:357px;top:150px">60.</p>
    <p class="label" style="left:53px;top:184px">Design Process</p>
    <p class="label" style="left:205px;top:184px">Project Process</p>
    <p class="label" style="left:357px;top:184px">Team Process</p>
    <p class="copy" style="left:53px;top:197px;width:125px">Measured progress on every design stage we lead.</p>
    <p class="copy" style="left:205px;top:197px;width:125px">Projects delivered on time and within budget.</p>
    <p class="copy" style="left:357px;top:197px;width:125px">Teams aligned around one shared goal.</p>
    <p class="footer-url">www.noraline.co</p><p class="page-no">18</p>
  </section>

  <section class="slide">
    <p class="brand">NORALINE</p>
    <p class="tag" style="left:222px;top:51px">Special Services</p>
    <h2 class="title center" style="left:0;top:64px;width:514px;font-size:20px;line-height:27px">A man should never neglect<br>his family for business</h2>
    <div class="service-card" style="left:0">
      <svg width="12" height="12" viewBox="0 0 12 12" fill="none" stroke="#22242b" stroke-width="1.1"><path d="M2 1v10M6 1v10M10 1v10M1 4h2M5 7h2M9 3h2"/></svg>
      <p class="label">BUSINESS SERVICES</p><p class="copy">Practical advice for growing firms.</p>
    </div>
    <div class="service-card active" style="left:128px">
      <svg width="12" height="12" viewBox="0 0 12 12" fill="none" stroke="#fff" stroke-width="1.1"><path d="M3 1h6v3a3 3 0 0 1-6 0zM6 7v3M3.5 11h5"/></svg>
      <p class="label light">BUSINESS SERVICES</p><p class="copy light">Practical advice for growing firms.</p>
      <span class="btn">Read More</span>
    </div>
    <div class="service-card" style="left:257px">
      <svg width="12" height="12" viewBox="0 0 12 12" fill="none" stroke="#22242b" stroke-width="1.1"><rect x="1" y="1" width="10" height="10"/><path d="M1 6h10M6 1v10"/></svg>
      <p class="label">BUSINESS SERVICES</p><p class="copy">Practical advice for growing firms.</p>
    </div>
    <div class="service-card" style="left:386px">
      <svg width="12" height="12" viewBox="0 0 12 12" fill="none" stroke="#22242b" stroke-width="1.1"><circle cx="6" cy="6" r="5"/><path d="M6 3v3l2 1.5"/></svg>
      <p class="label">BUSINESS SERVICES</p><p class="copy">Practical advice for growing firms.</p>
    </div>
    <p class="footer-url">www.noraline.co</p><p class="page-no">19</p>
  </section>

  <!-- row 3 -->
  <section class="slide">
    <p class="brand">NORALINE</p>
    <p class="tag" style="left:53px;top:53px">Special Services</p>
    <h2 class="title" style="left:53px;top:66px;width:200px">Our work is the presentation of our capabilities.</h2>
    <p class="copy" style="left:53px;top:187px">UX / UI Process</p><p class="copy" style="left:208px;top:187px">90%</p>
    <div class="bar-track" style="left:53px;top:198px"><div class="bar-fill" style="width:90%"></div></div>
    <p class="copy" style="left:53px;top:211px">Marketing Process</p><p class="copy" style="left:208px;top:211px">60%</p>
    <div class="bar-track" style="left:53px;top:222px"><div class="bar-fill" style="width:60%"></div></div>
    <div class="photo dim" style="left:258px;top:0;width:256px;height:289px" role="img" aria-label="Dark road running through a forest"></div>
    <p class="stat light" style="left:286px;top:66px">90.</p>
    <p class="label light" style="left:330px;top:68px">Design Process</p>
    <p class="copy light" style="left:330px;top:80px;width:150px">Steady progress on every design brief.</p>
    <p class="stat light" style="left:286px;top:138px">78.</p>
    <p class="label light" style="left:330px;top:140px">Design Process</p>
    <p class="copy light" style="left:330px;top:152px;width:150px">Reviews held with clients each week.</p>
    <p class="stat light" style="left:286px;top:204px">54.</p>
    <p class="label light" style="left:330px;top:206px">Design Process</p>
    <p class="copy light" style="left:330px;top:218px;width:150px">Concepts refined before final delivery.</p>
  </section>

  <section class="slide">
    <p class="brand">NORALINE</p>
    <div class="menu">
      <p class="menu-item active">Project Overview</p><p class="menu-item">Careers</p>
      <p class="menu-item">Our Featured Projects</p><p class="menu-item">Business Analysis</p>
    </div>
    <p class="tag" style="left:230px;top:51px">Project Overview</p>
    <h2 class="title" style="left:230px;top:64px;width:180px">A business that makes nothing…</h2>
    <p class="copy" style="left:230px;top:130px;width:250px">We help listed companies turn strategy into measurable results. Every project starts with a clear review of goals, markets and the people who will carry the plan forward in the years ahead.</p>
    <p class="stat" style="left:230px;top:206px">80+</p>
    <p class="label" style="left:280px;top:209px">Design Concept</p>
    <p class="copy" style="left:280px;top:220px">Delivered for clients</p>
    <p class="footer-url">www.noraline.co</p><p class="page-no">21</p>
  </section>

  <!-- row 4 -->
  <section class="slide">
    <p class="brand">NORALINE</p>
    <div class="menu">
      <p class="menu-item">Project Overview</p><p class="menu-item active">Careers</p>
      <p class="menu-item">Our Featured Projects</p><p class="menu-item">Business Analysis</p>
    </div>
    <h2 class="title" style="left:230px;top:48px">Careers</h2>
    <div class="check-row" style="top:96px"><span class="check-box on"></span><div><p class="label">It is rare to find a business partner who is selfless.</p><p class="copy">We look for people who put the client first.</p><p class="copy">Design Process</p></div></div>
    <div class="check-row" style="top:152px"><span class="check-box"></span><div><p class="label">Business opportunities are like buses; there's always another one coming.</p></div></div>
    <div class="check-row" style="top:196px"><span class="check-box"></span><div><p class="label">Life is an exciting business, and most exciting when it is lived for others.</p></div></div>
    <p class="footer-url">www.noraline.co</p><p class="page-no">22</p>
  </section>

  <section class="slide">
    <p class="brand">NORALINE</p>
    <div class="menu">
      <p class="menu-item">Project Overview</p><p class="menu-item">Careers</p>
      <p class="menu-item active">Our Featured Projects</p><p class="menu-item">Business Analysis</p>
    </div>
    <p class="tag" style="left:230px;top:51px">Project Overview</p>
    <h2 class="title" style="left:230px;top:64px;width:230px">Business Featured Projects</h2>
    <div class="photo dim" style="left:230px;top:145px;width:113px;height:95px" role="img" aria-label="Jellyfish in dark water"></div>
    <div class="photo" style="left:347px;top:145px;width:113px;height:95px" role="img" aria-label="Glass skyscrapers against the sky"></div>
    <p class="footer-url">www.noraline.co</p><p class="page-no">23</p>
  </section>

  <!-- row 5 -->
  <section class="slide">
    <p class="brand">NORALINE</p>
    <div class="menu">
      <p class="menu-item">Project Overview</p><p class="menu-item">Careers</p>
      <p class="menu-item">Our Featured Projects</p><p class="menu-item active">Business Analysis</p>
    </div>
    <p class="tag" style="left:230px;top:51px">Featured Project</p>
    <h2 class="title" style="left:230px;top:64px">Business Concept</h2>
    <p class="copy" style="left:230px;top:96px;width:250px">Quarterly results for our core service lines, shown side by side for quick review.</p>
    <svg style="left:225px;top:140px" width="260" height="110" viewBox="0 0 260 110" font-family="Roboto,sans-serif" font-size="5" fill="#8b8f99">
      <g stroke="#d3d6dc" stroke-width="0.6"><path d="M14 10H250M14 30H250M14 50H250M14 70H250M14 90H250"/></g>
      <text x="0" y="12">100</text><text x="2" y="32">80</text><text x="2" y="52">60</text><text x="2" y="72">40</text><text x="2" y="92">20</text>
      <g fill="#22242b">
        <rect x="28" y="58" width="6" height="32"/><rect x="37" y="66" width="6" height="24" fill="#8b8f99"/>
        <rect x="68" y="64" width="6" height="26"/><rect x="77" y="70" width="6" height="20" fill="#8b8f99"/>
        <rect x="108" y="50" width="6" height="40"/><rect x="117" y="60" width="6" height="30" fill="#8b8f99"/>
        <rect x="148" y="36" width="6" height="54"/><rect x="157" y="54" width="6" height="36" fill="#8b8f99"/>
        <rect x="188" y="22" width="6" height="68"/><rect x="197" y="44" width="6" height="46" fill="#8b8f99"/>
        <rect x="228" y="56" width="6" height="34"/><rect x="237" y="64" width="6" height="26" fill="#8b8f99"/>
      </g>
      <text x="26" y="100">Item 1</text><text x="66" y="100">Item 2</text><text x="106" y="100">Item 3</text><text x="146" y="100">Item 4</text><text x="186" y="100">Item 5</text><text x="226" y="100">Item 6</text>
    </svg>
    <p class="footer-url">www.noraline.co</p><p class="page-no">24</p>
  </section>

  <section class="slide">
    <div class="photo" style="left:0;top:0;width:258px;height:289px" role="img" aria-label="Office tower rising into a cloudy sky"></div>
    <p class="tag" style="left:281px;top:51px">Our Concepts</p>
    <h2 class="title" style="left:281px;top:64px;width:180px">A business that makes nothing…</h2>
    <p class="copy" style="left:281px;top:130px;width:210px">Our advice stays practical and rooted in the numbers that matter to your board.</p>
    <div class="rule" style="left:258px;top:182px;width:256px"></div>
    <p class="label" style="left:281px;top:210px">Consulting</p>
    <p class="copy" style="left:281px;top:222px;width:100px">Strategy built with your leaders.</p>
    <p class="label" style="left:400px;top:210px">Branding</p>
    <p class="copy" style="left:400px;top:222px;width:100px">A voice your market remembers.</p>
    <p class="footer-url">www.noraline.co</p><p class="page-no">25</p>
  </section>

  <!-- row 6 -->
  <section class="slide">
    <p class="brand">NORALINE</p>
    <div class="photo dim" style="left:0;top:47px;width:132px;height:191px" role="img" aria-label="City towers at dusk"></div>
    <div class="panel-dark" style="left:132px;top:47px;width:252px;height:191px"></div>
    <div class="photo dim" style="left:384px;top:47px;width:130px;height:191px" role="img" aria-label="Person walking through a dim hallway"></div>
    <p class="tag" style="left:232px;top:93px">Our Portfolio</p>
    <h2 class="title light center" style="left:132px;top:106px;width:252px">Our work is the presentation of our capabilities.</h2>
    <p class="footer-url">www.noraline.co</p><p class="page-no">26</p>
  </section>

  <section class="slide is-dark">
    <p class="tag" style="left:219px;top:57px">Welcome Message</p>
    <h2 class="title light center" style="left:0;top:72px;width:514px">Great companies are<br>built on great products</h2>
    <p class="copy light" style="left:97px;top:150px;width:320px;text-align:center">We partner with leadership teams to sharpen strategy, simplify operations and build products that their customers value. Each engagement ends with a plan your people can own and act on.</p>
  </section>

  <!-- row 7 -->
  <section class="slide">
    <p class="brand">NORALINE</p>
    <div class="photo pale" style="left:53px;top:49px;width:269px;height:158px" role="img" aria-label="Cargo bicycle parked on a bright beach"></div>
    <p class="tag" style="left:262px;top:106px">Overview</p>
    <h2 class="title" style="left:262px;top:118px;width:230px">Our work is the presentation of our capabilities.</h2>
    <p class="footer-url">www.noraline.co</p><p class="page-no">28</p>
  </section>

  <section class="slide">
    <p class="brand">NORALINE</p>
    <p class="tag" style="left:53px;top:51px">Project Overview</p>
    <h2 class="title" style="left:53px;top:64px;width:170px">Easy trip from business</h2>
    <p class="copy" style="left:230px;top:64px;width:250px">Travel and site visits planned around your schedule, so teams meet in person when it matters most and keep momentum between sessions.</p>
    <div class="photo" style="left:53px;top:136px;width:147px;height:153px" role="img" aria-label="Tall buildings seen from street level"></div>
    <div class="photo dim" style="left:200px;top:136px;width:145px;height:153px" role="img" aria-label="Aircraft tail on an airfield"></div>
    <div class="photo" style="left:345px;top:136px;width:169px;height:153px" role="img" aria-label="Glass tower facade"></div>
  </section>

  <!-- row 8 -->
  <section class="slide">
    <p class="brand">NORALINE</p>
    <div class="photo" style="left:53px;top:47px;width:102px;height:90px" role="img" aria-label="Skyscraper corner"></div>
    <div class="photo" style="left:155px;top:47px;width:102px;height:90px" role="img" aria-label="Modern office building"></div>
    <svg style="left:300px;top:58px" width="14" height="12" viewBox="0 0 14 12" fill="none" stroke="#22242b" stroke-width="1.1"><path d="M1 1h12v8H5l-3 2V9H1z"/></svg>
    <p class="label" style="left:266px;top:75px;width:84px;text-align:center;font-size:5.5px">BUSINESS SERVICES</p>
    <p class="copy" style="left:266px;top:85px;width:84px;text-align:center;font-size:5px;line-height:7px">Guidance for each stage of growth.</p>
    <div class="photo" style="left:359px;top:47px;width:101px;height:90px" role="img" aria-label="Stairway inside a concrete building"></div>
    <div class="photo" style="left:53px;top:137px;width:102px;height:89px" role="img" aria-label="Glass tower against the sky"></div>
    <div class="photo dim" style="left:155px;top:137px;width:102px;height:89px" role="img" aria-label="Jellyfish in dark water"></div>
    <div class="photo" style="left:257px;top:137px;width:102px;height:89px" role="img" aria-label="Office interior"></div>
    <div class="photo dim" style="left:359px;top:137px;width:101px;height:89px" role="img" aria-label="Dark architectural detail"></div>
    <p class="footer-url">www.noraline.co</p><p class="page-no">30</p>
  </section>

  <section class="slide">
    <div class="photo" style="left:53px;top:47px;width:100px;height:90px" role="img" aria-label="Building facade"></div>
    <div class="photo" style="left:153px;top:47px;width:102px;height:90px" role="img" aria-label="Person standing against a pale sky"></div>
    <p class="label" style="left:268px;top:78px">Creative Design</p>
    <p class="copy" style="left:268px;top:90px;width:100px">Concepts with a clear purpose.</p>
    <div class="photo dim" style="left:53px;top:137px;width:100px;height:89px" role="img" aria-label="Dark building at night"></div>
    <div class="photo dim" style="left:153px;top:137px;width:102px;height:89px" role="img" aria-label="Building corner"></div>
    <div class="photo" style="left:255px;top:137px;width:111px;height:89px" role="img" aria-label="Open road through a forest"></div>
    <p class="label" style="left:383px;top:160px">Creative Design</p>
    <p class="copy" style="left:383px;top:172px;width:100px">Concepts with a clear purpose.</p>
    <p class="footer-url">www.noraline.co</p><p class="page-no">31</p>
  </section>

  <!-- row 9 -->
  <section class="slide">
    <p class="brand">NORALINE</p>
    <div class="photo" style="left:0;top:47px;width:103px;height:100px" role="img" aria-label="Office towers"></div>
    <div class="photo" style="left:103px;top:47px;width:103px;height:100px" role="img" aria-label="Skyscraper seen from below"></div>
    <div class="photo pale" style="left:206px;top:47px;width:103px;height:100px" role="img" aria-label="Bright sky over rooftops"></div>
    <div class="photo dim" style="left:309px;top:47px;width:103px;height:100px" role="img" aria-label="Dark building detail"></div>
    <div class="photo" style="left:412px;top:47px;width:102px;height:100px" role="img" aria-label="Stairway in a concrete hall"></div>
    <p class="tag" style="left:53px;top:163px">Welcome Message</p>
    <h2 class="title" style="left:53px;top:176px">Great companies are</h2>
    <p class="copy" style="left:300px;top:163px;width:190px">We build plans that leaders can act on from day one.</p>
  </section>

  <section class="slide">
    <p class="brand">NORALINE</p>
    <p class="tag" style="left:53px;top:51px">Special Services</p>
    <h2 class="title" style="left:53px;top:64px;width:210px">Our work is the presentation of our capabilities.</h2>
  </section>

</main>
</div>
</body>
</html>
```